Radiant Harvest Gathering 2021

I am looking to create a flyer for a one day prayer retreat our church is organizing. This flyer will be posted on social media, websites, mobile apps, and will also be printed so it can be mailed to people.

I am looking for something professional, with good use of our logo and band colors (logo colors).

I am counting on the designer's skill, creativity, art and knowledge of media communication to produce a flyer that will effectively and quickly convey the message we are trying to spread.

CONTENT OF THE FLYER:
Event title: Radiant Harvest Gathering
Date: Tuesday July 2nd, 2021
Time: 11:00AM - 7:00PM
Bellmore Hotel, 4817 Wexley Avenue, Portland, Maine 04109 (Room: Tamarind)
Event Key words to highlight what the event is about: Prayer, Fasting, Worship, Prophecy, Revival.
Key phrases:
A one day prayer retreat.
Jesus Chris is Lord

Contact info:
www.quvello.org
Phone: 207 555 0148
Email: contact@brookmeadow.org

```html
<!DOCTYPE html>
<html lang="en">
<head>
<meta charset="utf-8">
<title>Radiant Harvest Gathering – One Day Prayer Retreat</title>
<link rel="stylesheet" href="https://fonts.googleapis.com/css2?family=Montserrat:wght@400;500;600;700&family=Poppins:wght@500;700&family=Great+Vibes&display=swap">
<style>
  :root {
    --ink: #060606;
    --paper: #ffffff;
    --ember: #e0533a;
    --sunset-deep: #a8243a;
    --sunset-mid: #e8551a;
    --sunset-glow: #ffd27a;
    --brand-navy: #1f2d7a;
  }
  * { margin: 0; padding: 0; box-sizing: border-box; }
  html, body {
    width: 848px; height: 1200px; overflow: hidden;
    background: var(--ink);
  }
  .flyer {
    position: relative;
    width: 848px; height: 1200px;
    background: var(--ink);
    color: var(--paper);
    font-family: 'Montserrat', sans-serif;
    overflow: hidden;
  }
  .hero-photo {
    position: absolute; left: 0; top: 0; width: 848px; height: 470px;
    background:
      radial-gradient(ellipse 260px 200px at 506px 250px, #fff6d8 0%, var(--sunset-glow) 25%, rgba(255,160,40,0.85) 55%, rgba(255,140,30,0) 100%),
      linear-gradient(180deg, var(--sunset-deep) 0%, var(--sunset-mid) 22%, #f07a1c 48%, #3a1206 72%, var(--ink) 100%);
  }
  .brand {
    position: absolute; left: 28px; top: 34px;
    display: flex; align-items: center; gap: 8px;
  }
  .brand-dot {
    width: 14px; height: 14px; border-radius: 50%;
    background: var(--brand-navy);
  }
  .brand-name {
    font-family: 'Poppins', sans-serif; font-weight: 700;
    font-size: 34px; color: var(--brand-navy); letter-spacing: 1px;
  }
  .line {
    position: absolute; left: 0; right: 0; text-align: center; white-space: nowrap;
  }
  .declaration {
    top: 372px; font-size: 38px; line-height: 46px; font-weight: 400;
    color: var(--ember); letter-spacing: 12px; padding-left: 12px;
  }
  .kicker {
    top: 456px; font-family: 'Poppins', sans-serif; font-weight: 500;
    font-size: 42px; line-height: 54px; letter-spacing: -0.5px;
  }
  .title {
    top: 508px; font-family: 'Poppins', sans-serif; font-weight: 700;
    font-size: 70px; line-height: 80px; letter-spacing: -1px;
  }
  .title-script {
    top: 570px; font-family: 'Great Vibes', cursive;
    font-size: 104px; line-height: 110px; color: var(--ember);
  }
  .date {
    top: 737px; font-size: 33px; line-height: 40px; font-weight: 500;
    letter-spacing: 7px; padding-left: 7px;
  }
  .time {
    top: 792px; font-size: 33px; line-height: 40px; font-weight: 500;
    letter-spacing: 6px; padding-left: 6px;
  }
  .contact-tab {
    position: absolute; left: 229px; top: 886px; width: 411px; height: 47px;
    background: var(--ember); color: var(--ink);
    display: flex; align-items: center; justify-content: center;
    font-weight: 700; font-size: 30px; letter-spacing: 7px; padding-left: 7px;
  }
  .detail {
    font-size: 22px; line-height: 28px; font-weight: 500; letter-spacing: 4px; padding-left: 4px;
  }
  .phone { top: 966px; }
  .email { top: 1011px; }
  .venue { top: 1059px; }
  .venue-city { top: 1087px; }
  .web {
    top: 1138px; color: var(--ember); font-size: 21px; line-height: 28px;
    font-weight: 500; letter-spacing: 5px; padding-left: 5px;
  }
</style>
</head>
<body>
  <main class="flyer">
    <div class="hero-photo" role="img" aria-label="Sunset sky behind a hilltop silhouette with a wooden cross and small figures"></div>

    <div class="brand">
      <span class="brand-dot"></span>
      <span class="brand-name">QUVELLO</span>
    </div>

    <p class="line declaration">JESUS IS LORD</p>
    <p class="line kicker">A ONEDAY PRAYER RETREAT</p>
    <h1 class="line title">RADIANT HARVEST</h1>
    <p class="line title-script">Gathering</p>

    <p class="line date">TUESDAY 2ND JULY</p>
    <p class="line time">11:00AM – 7:00PM</p>

    <div class="contact-tab">CONTACT US</div>

    <p class="line detail phone">Phone: 207 555 0148</p>
    <p class="line detail email">Email: contact@brookmeadow.org</p>
    <p class="line detail venue">Bellmore Hotel, 4817 Wexley Avenue,</p>
    <p class="line detail venue-city">Portland, Maine 04109</p>

    <p class="line web">FOR INFO VISIT AT : www.quvello.org</p>
  </main>
</body>
</html>
```